Property Management Company looking for a high-end business card, letterhead and envelope design.

We provide high-end / boutique property management for real estate investors or individuals looking for someone to manage their portfolio. we are looking for a cohesive high-end design for our business cards, letterhead and envelopes.

Target Market(s)

Real Estate Investors

Industry/Entity Type

Real Estate

Requirements
Must have
• business card, letterhead and envelope design - logo attached

```html
<!DOCTYPE html>
<html lang="en">
<head>
<meta charset="utf-8">
<title>Northvale Property Management – Business Card</title>
<link href="https://fonts.googleapis.com/css2?family=Figtree:wght@400;500;600;700&display=swap" rel="stylesheet">
<style>
  :root {
    --navy: #0d4a7a;
    --band-blue: #0b6aa3;
    --text-gray: #4f4f4f;
    --paper: #ffffff;
    --stage: #e4e4e4;
    --back-light: #a2a2a2;
    --back-dark: #7c7c7c;
  }
  * { margin: 0; padding: 0; box-sizing: border-box; }
  html, body {
    width: 1200px; height: 1200px; overflow: hidden;
    background: var(--stage);
    font-family: "Figtree", sans-serif;
  }
  .card {
    position: absolute;
    left: 257px;
    width: 800px; height: 457px;
    transform: scale(0.8575);
    transform-origin: 0 0;
    box-shadow: 0 18px 40px rgba(0,0,0,0.22);
    overflow: hidden;
  }
  .card-front { top: 165px; background: var(--paper); }
  .card-back { top: 653px; }

  .brand { position: absolute; left: 46px; top: 86px; color: var(--navy); }
  .brand-name {
    font-size: 40px; font-weight: 700; letter-spacing: 6px; line-height: 1;
  }
  .brand-tagline {
    margin-top: 6px;
    font-size: 18px; font-weight: 500; letter-spacing: 3.6px; line-height: 1;
  }

  .divider {
    position: absolute; left: 0; top: 228px;
    width: 500px; height: 3px; background: var(--navy);
  }
  .name-band { position: absolute; left: 0; top: 0; width: 800px; height: 457px; }
  .holder {
    position: absolute; right: 35px; top: 168px;
    text-align: right; color: #fff;
  }
  .holder-name { font-size: 26px; font-weight: 600; line-height: 1.1; }
  .holder-title { font-size: 17px; font-weight: 400; margin-top: 3px; }

  .address {
    position: absolute; left: 43px; top: 276px;
    font-size: 17px; line-height: 22px; color: var(--text-gray);
  }
  .contacts {
    position: absolute; left: 44px; top: 333px;
    list-style: none; font-size: 17px; color: var(--text-gray);
  }
  .contacts li { display: flex; align-items: center; height: 23px; }
  .contacts svg { width: 15px; height: 15px; margin-right: 11px; fill: var(--navy); }

  .back-surface {
    position: absolute; inset: 0;
    background: linear-gradient(110deg, var(--back-light) 0%, #8e8e8e 55%, var(--back-dark) 100%);
  }
  .back-brand {
    position: absolute; right: 80px; bottom: 62px;
    font-size: 24px; font-weight: 700; letter-spacing: 4px; color: #fff;
  }
</style>
</head>
<body>
  <section class="card card-front">
    <div class="brand">
      <div class="brand-name">NORTHVALE</div>
      <div class="brand-tagline">PROPERTY MANAGEMENT</div>
    </div>
    <div class="divider"></div>
    <svg class="name-band" viewBox="0 0 800 457" aria-hidden="true">
      <polygon points="527,161 800,161 800,230 475,230" fill="var(--band-blue)"/>
    </svg>
    <div class="holder">
      <div class="holder-name">DANIEL HARPER</div>
      <div class="holder-title">President</div>
    </div>
    <p class="address">2140 Birchwood Drive<br>Anchorage, Alaska 34512</p>
    <ul class="contacts">
      <li><svg viewBox="0 0 16 16"><path d="M3.5 1 6 1.5 7 5 5.3 6.3c.9 1.9 2.4 3.4 4.3 4.3L11 9l3.5 1 .5 2.5c-.4 1.4-1.6 2.4-3 2.3C6.4 14.4 1.6 9.6 1.2 4 1.1 2.6 2.1 1.4 3.5 1z"/></svg>369-555-0142</li>
      <li><svg viewBox="0 0 16 16"><path d="M4 1h8v14H4zM5.5 2.5v9.5h5V2.5zM7.2 13h1.6v1H7.2z" fill-rule="evenodd"/></svg>369-555-0187</li>
      <li><svg viewBox="0 0 16 16"><path d="M1 4h14v9H1zM2.5 5l5.5 4 5.5-4z" fill-rule="evenodd"/></svg>info@northvalepm.com</li>
      <li><svg viewBox="0 0 16 16"><circle cx="8" cy="8" r="7"/><path d="M5 4.5c1.5 0 2 1.5 1 2.5S4.5 9 6 10.5M10 3c-.5 1.5 1 2 2 2.5M10 12c0-1.5 1.5-2 2.5-1.5" stroke="#fff" stroke-width="1.1" fill="none"/></svg>www.northvalepm.com</li>
    </ul>
  </section>

  <section class="card card-back">
    <div class="back-surface" role="img" aria-label="Embossed repeating brand pattern on a grey card surface"></div>
    <div class="back-brand">NORTHVALE</div>
  </section>
</body>
</html>
```